Capability Statement Flyer

We want to develop a flyer to show potential clients our work capability. We want to incorporate our logo. You can reference our website for any other graphics you may want to incorporate. Our blue CMYK is 100-80-0-22

Colors
0555a3

Requirements
Must have
• Capability Statement
• Our expertise and technical resources fuel the delivery of our services. As a leading provider of construction services, Halvern Construction focuses on providing solutions for civil infrastructure, industrial infrastructure, and commercial market segments. Driven by a commitment to continuous improvement, Halvern Construction has the expertise in the following key areas:
• • Design Build/Problem Solving
• • Storm and Process Water Systems
• • Heavy and Structural Concrete
• • Bridge Construction
• • Building Construction and Restoration
• • Hardscapes
• • All Civil Construction and Utility
Nice to have
• Creativity to present to potential clients. Not just words on the page

```html
<!DOCTYPE html>
<html lang="en">
<head>
<meta charset="utf-8">
<title>Halvern Construction – Capability Statement</title>
<link href="https://fonts.googleapis.com/css2?family=Oswald:wght@400;500&family=Open+Sans:wght@400;600&display=swap" rel="stylesheet">
<style>
:root{
  --navy:#253a86;
  --ink:#222;
  --text:#444;
  --paper:#fff;
  --backdrop:#a9abaf;
  --black:#000;
  --photo-warm:#b08a5c;
  --photo-road:#3a5470;
  --photo-site:#6b5a48;
}
*{box-sizing:border-box;margin:0;padding:0}
html,body{width:1200px;height:797px;overflow:hidden}
body{background:var(--backdrop);font-family:"Open Sans",sans-serif;color:var(--text);position:relative}
.page{position:absolute;top:47px;width:536px;height:691px;background:var(--paper);overflow:hidden}
.page--front{left:48px}
.page--back{left:617px;width:535px}
.abs{position:absolute}
.head{font-family:"Oswald",sans-serif;font-weight:500;color:var(--navy);text-transform:uppercase;line-height:1}

/* brand */
.brand{display:flex;align-items:center;gap:6px}
.brand__mark{width:30px;height:30px;background:var(--navy)}
.brand__name{font-family:"Oswald",sans-serif;font-weight:500;color:var(--navy);line-height:1;text-transform:uppercase}
.brand__name span{display:block}
.brand--header{left:47px;top:36px}
.brand--header .brand__name span:first-child{font-size:30px;letter-spacing:.5px}
.brand--header .brand__name span:last-child{font-size:11px;letter-spacing:1px;margin-top:2px}

.title{left:272px;top:46px;font-size:30px;letter-spacing:.2px}
.title b{font-weight:500;color:var(--ink)}

/* photo strip */
.photo{position:absolute;top:107px;height:125px;border-top:6px solid var(--navy)}
.photo--house{left:0;width:174px;background:linear-gradient(160deg,#e7a04e,var(--photo-warm) 45%,#5b6b3c)}
.photo--roads{left:184px;width:173px;border-top-color:var(--black);background:linear-gradient(135deg,#4b6a88,var(--photo-road) 50%,#253548)}
.photo--site{left:367px;width:169px;background:linear-gradient(160deg,#8a7866,var(--photo-site) 55%,#3f342a)}

/* about */
.about__head{left:33px;top:257px;font-size:22px}
.about__text{left:33px;width:238px;font-size:8.6px;line-height:11.8px}
.expertise{left:33px;top:457px;font-family:"Oswald",sans-serif;font-size:16.5px;line-height:22.5px;color:var(--navy);width:260px}
.areas{left:38px;top:516px;list-style:none;font-size:10.4px;color:#444}
.areas li{height:18.3px;display:flex;align-items:center;gap:15px}
.areas li::before{content:"";width:11px;height:11px;background:var(--ink);display:inline-block}

/* steps */
.help__head{left:300px;top:261px;font-size:17px;font-weight:400}
.step{position:absolute;left:300px;width:228px;height:70px}
.step__badge{position:absolute;left:2px;top:0;width:38px;text-align:center}
.step__badge svg{display:block;margin:0 auto}
.step__pill{display:inline-block;margin-top:-4px;background:var(--black);color:#fff;font-family:"Open Sans",sans-serif;font-weight:600;font-size:8px;border-radius:6px;padding:0 5px;line-height:11px;position:relative}
.step__text{position:absolute;left:58px;top:0;width:150px;font-size:8.4px;line-height:12px}

.quote{left:298px;top:528px;width:224px;height:134px;background:var(--black);color:#fff;font-size:8.5px;line-height:10.8px;padding:14px 12px 0 14px}
.quote__mark{font-family:"Oswald",sans-serif;font-size:28px;line-height:1;position:absolute}
.quote__mark--open{left:12px;top:6px}
.quote__mark--close{right:12px;bottom:8px}
.quote p{text-indent:30px}

.band{position:absolute;left:0;width:100%;background:var(--navy);color:#fff}
.band--front{top:662px;height:29px;display:flex;align-items:center;justify-content:center;gap:8px;font-size:10.5px}
.band--front i{display:block;width:40px;height:1px;background:rgba(255,255,255,.6)}

/* back page */
.photo--worker{position:absolute;left:37px;top:24px;width:250px;height:254px;background:linear-gradient(150deg,#9a8a74,#5c4d3e 55%,#2e2620)}
.mission{left:314px;top:0;width:202px;height:212px;background:var(--navy);color:#fff;padding:33px 0 0 16px}
.mission__head{font-family:"Oswald",sans-serif;font-weight:500;font-size:20px;line-height:1;margin-bottom:16px}
.mission p{font-size:10.8px;line-height:15.8px;width:180px}
.feature__head{left:37px;top:301px;font-size:21px;line-height:27.5px;font-weight:400}
.feature__sub{left:37px;top:369px;font-size:15.8px;line-height:21px;font-weight:400;color:var(--ink)}
.feature__text{left:37px;top:413px;width:252px;font-size:8.5px;line-height:11.9px}

.services__head{left:314px;top:242px;font-size:18.5px;font-weight:400;color:var(--ink)}
.service{position:absolute;left:314px;width:210px;height:62px}
.service svg{position:absolute;left:4px;top:4px}
.service__title{position:absolute;left:47px;top:0;font-family:"Oswald",sans-serif;font-weight:500;font-size:15.5px;line-height:18px;color:var(--navy);text-transform:uppercase}
.service__text{position:absolute;left:47px;top:19px;width:150px;font-size:8.3px;line-height:13px}

.band--back{top:617px;height:74px;font-size:9.4px;line-height:13px}
.address{position:absolute;left:37px;top:19px}
.contact{position:absolute;left:157px;top:19px;list-style:none}
.contact li{display:flex;align-items:center;gap:6px}
.brand--footer{position:absolute;left:361px;top:10px}
.brand--footer .brand__mark{width:26px;height:26px;background:#fff}
.brand--footer .brand__name{color:#fff}
.brand--footer .brand__name span:first-child{font-size:24px}
.brand--footer .brand__name span:last-child{font-size:8.5px;letter-spacing:1px;margin-top:1px}
.site--back{position:absolute;left:351px;top:54px;font-size:9.6px}
</style>
</head>
<body>

<section class="page page--front">
  <div class="brand brand--header abs">
    <div class="brand__mark"></div>
    <div class="brand__name"><span>Halvern</span><span>Construction</span></div>
  </div>
  <h1 class="head title abs">Capability <b>Statement</b></h1>

  <div class="photo photo--house" role="img" aria-label="Timber-framed house under construction at sunset"></div>
  <div class="photo photo--roads" role="img" aria-label="Aerial view of highway interchange"></div>
  <div class="photo photo--site" role="img" aria-label="Workers in hard hats on a building site viewed from above"></div>

  <h2 class="head about__head abs">About Us</h2>
  <p class="about__text abs" style="top:286px">Our expertise and technical resources fuel the delivery of our services. As a leading provider of construction services, Halvern Construction focuses on providing solutions for civil infrastructure, industrial infrastructure, and commercial market segments. Driven by a commitment to continuous improvement.</p>
  <p class="about__text abs" style="top:369px">Lorem ipsum dolor sit amet, consectetur adipiscing elit, sed do eiusmod tempor incididunt ut labore et dolore magna aliqua. Ut enim ad minim veniam, quis nostrud exercitation ullamco laboris nisi ut aliquip ex ea commodo consequat. Duis aute irure dolor in reprehenderit in voluptate velit esse cillum dolore eu.</p>

  <p class="expertise abs">Halvern Construction has the expertise in the following key areas:</p>
  <ul class="areas abs">
    <li>Design Build/Problem Solving</li>
    <li>Storm and Process Water Systems</li>
    <li>Heavy and Structural Concrete</li>
    <li>Bridge Construction</li>
    <li>Building Construction and Restoration</li>
    <li>Hardscapes</li>
    <li>All Civil Construction and Utility</li>
  </ul>

  <h2 class="head help__head abs">How We Can Help You</h2>

  <div class="step" style="top:294px">
    <div class="step__badge">
      <svg width="36" height="36" viewBox="0 0 36 36"><circle cx="18" cy="18" r="18" fill="#e6e7ea"/><rect x="12" y="9" width="12" height="16" rx="1" fill="none" stroke="#253a86" stroke-width="1.8"/><path d="M15 14h6M15 17h6M15 20h4" stroke="#253a86" stroke-width="1.5"/></svg>
      <span class="step__pill">STEP 1</span>
    </div>
    <p class="step__text">Lorem ipsum dolor sit amet, consectetur adipiscing elit, sed do eiusmod tempor incididunt ut labore et dolore magna aliqua. Ut enim ad minim veniam, quis nostrud exercita-</p>
  </div>
  <div class="step" style="top:368px">
    <div class="step__badge">
      <svg width="36" height="36" viewBox="0 0 36 36"><circle cx="18" cy="18" r="18" fill="#e6e7ea"/><rect x="12" y="9" width="12" height="17" rx="1.5" fill="#253a86"/><rect x="14" y="11" width="8" height="4" fill="#fff"/><path d="M14.5 18h2M19.5 18h2M14.5 21h2M19.5 21h2M14.5 24h2M19.5 24h2" stroke="#fff" stroke-width="1.5"/></svg>
      <span class="step__pill">STEP 2</span>
    </div>
    <p class="step__text">Lorem ipsum dolor sit amet, consectetur adipiscing elit, sed do eiusmod tempor incididunt ut labore et dolore magna aliqua. Ut enim ad minim veniam, quis nostrud exercita-</p>
  </div>
  <div class="step" style="top:442px">
    <div class="step__badge">
      <svg width="36" height="36" viewBox="0 0 36 36"><circle cx="18" cy="18" r="18" fill="#e6e7ea"/><path d="M8 18l10-9 10 9" fill="none" stroke="#253a86" stroke-width="2.2"/><path d="M11 17v9h14v-9l-7-6z" fill="#253a86"/><rect x="16" y="20" width="4" height="6" fill="#fff"/></svg>
      <span class="step__pill">STEP 3</span>
    </div>
    <p class="step__text">Lorem ipsum dolor sit amet, consectetur adipiscing elit, sed do eiusmod tempor incididunt ut labore et dolore magna aliqua. Ut enim ad minim veniam, quis nostrud exercita-</p>
  </div>

  <blockquote class="quote abs">
    <span class="quote__mark quote__mark--open">&ldquo;</span>
    <p>Lorem ipsum dolor sit amet, consecr adipiscing elit, sed do eiusmod tempor incididunt ut labore et dolore magna aliqua. Ut enim ad minim veniam, quis nostrud exercitation ullamco laboris nisi ut aliquip ex ea commodo consequat. Duis aute irure dolor in reprehenderit in voluptate velit esse cillum dolore eu fugiat nulla pariatur. Excepteur sint occaecat cupidatat non proident, sunt in culpa qui officia deserunt mollit anim laborum.</p>
    <span class="quote__mark quote__mark--close">&rdquo;</span>
  </blockquote>

  <footer class="band band--front"><i></i>www.halvernconstruction.com<i></i></footer>
</section>

<section class="page page--back">
  <div class="photo--worker" role="img" aria-label="Construction worker in a hard hat working on a wooden formwork ramp"></div>

  <aside class="mission abs">
    <h2 class="mission__head">MISSION</h2>
    <p>Lorem ipsum dolor sit amet, consectetur adipiscing elit, sed do eiusmod tempor incididunt ut labore et dolore magna aliqua. Ut enim ad minim veniam, quis nostrud exercitation ullamco laboris nisi ut aliquip ex ea commodo consequat.</p>
  </aside>

  <h2 class="head feature__head abs">Lorem ipsum dolor sit<br>amet, dunt ut labore et</h2>
  <h3 class="head feature__sub abs">Lorem ipsum dolor sit amet,<br>consectetur adipiscing</h3>
  <p class="feature__text abs">"Lorem ipsum dolor sit amet, consectetur adipiscing elit, sed do eiusmod tempor incididunt ut labore et dolore magna aliqua. Ut enim ad minim veniam, quis nostrud exercitation ullamco laboris nisi ut aliquip ex ea commodo consequat. Duis aute irure dolor in reprehenderit in voluptate velit esse cillum dolore eu fugiat nulla pariatur. Excepteur sint occaecat cupidatat non proident, sunt in culpa qui officia deserunt mollit anim id est laborum."Lorem ipsum dolor sit amet, consectetur adipiscing elit, sed do eiusmod tempor incididunt ut labore et dolore magna aliqua. Ut enim ad minim veniam, quis nostrud exercitation ullamco laboris nisi ut aliquip ex ea commodo consequat. Duis aute irure dolor in reprehenderit in voluptate velit esse cillum dolore eu fugiat nulla pariatur. Excepteur sint occaecat cupidatat non proident, sunt in culpa qui officia deserunt mollit anim id est laborum.</p>

  <h2 class="head services__head abs">Services We Offer</h2>

  <div class="service" style="top:284px">
    <svg width="28" height="28" viewBox="0 0 28 28"><path d="M10 4h8l-2 5h-4z" fill="#253a86"/><path d="M11 9h6c5 3 7 8 6 12-1 3-4 4-9 4s-8-1-9-4c-1-4 1-9 6-12z" fill="#253a86"/><text x="14" y="21" font-size="9" font-family="Open Sans, sans-serif" fill="#fff" text-anchor="middle">$</text></svg>
    <span class="service__title">Financial</span>
    <p class="service__text">Lorem ipsum dolor sit amet, consectetur adipiscing elit, sed do eiusmod tempor incididunt.</p>
  </div>
  <div class="service" style="top:349px">
    <svg width="28" height="28" viewBox="0 0 28 28"><rect x="3" y="5" width="16" height="20" rx="1" fill="none" stroke="#253a86" stroke-width="2"/><path d="M6 10h9M6 14h7M6 18h5" stroke="#253a86" stroke-width="1.6"/><path d="M12 20l12-12 2 2-12 12-3 1z" fill="#253a86"/></svg>
    <span class="service__title">Written Documents</span>
    <p class="service__text">Lorem ipsum dolor sit amet, consectetur adipiscing elit, sed do eiusmod tempor incididunt .</p>
  </div>
  <div class="service" style="top:414px">
    <svg width="28" height="28" viewBox="0 0 28 28"><path d="M4 3h11l5 5v8" fill="none" stroke="#253a86" stroke-width="2"/><path d="M4 3v22h10" fill="none" stroke="#253a86" stroke-width="2"/><path d="M7 11h8M7 15h6M7 19h5" stroke="#253a86" stroke-width="1.6"/><circle cx="20" cy="21" r="5.5" fill="#253a86"/><path d="M17.5 21l2 2 3-3.5" fill="none" stroke="#fff" stroke-width="1.5"/></svg>
    <span class="service__title">Loan Approval</span>
    <p class="service__text">Lorem ipsum dolor sit amet, consectetur adipiscing elit, sed do eiusmod tempor incididunt.</p>
  </div>
  <div class="service" style="top:479px">
    <svg width="28" height="28" viewBox="0 0 28 28"><rect x="3" y="6" width="19" height="18" rx="1" fill="none" stroke="#253a86" stroke-width="2"/><rect x="3" y="6" width="19" height="4" fill="#253a86"/><path d="M8 3v5M17 3v5" stroke="#253a86" stroke-width="2"/><path d="M6 13h3M11 13h3M6 17h3M11 17h3M6 21h3" stroke="#253a86" stroke-width="2"/><circle cx="21" cy="21" r="5" fill="#fff" stroke="#253a86" stroke-width="1.8"/><path d="M21 18.5V21h2" stroke="#253a86" stroke-width="1.4" fill="none"/></svg>
    <span class="service__title">Schedule Management</span>
    <p class="service__text">Lorem ipsum dolor sit amet, consectetur adipiscing elit, sed do eiusmod tempor incididunt.</p>
  </div>
  <div class="service" style="top:544px">
    <svg width="28" height="28" viewBox="0 0 28 28"><path d="M5 14a9 9 0 0 1 15-6.5" fill="none" stroke="#253a86" stroke-width="2"/><path d="M18 4l3 4-4.5 1z" fill="#253a86"/><path d="M23 14a9 9 0 0 1-15 6.5" fill="none" stroke="#253a86" stroke-width="2"/><path d="M10 24l-3-4 4.5-1z" fill="#253a86"/><circle cx="14" cy="14" r="5" fill="none" stroke="#253a86" stroke-width="1.6"/><text x="14" y="17" font-size="8" font-family="Open Sans, sans-serif" fill="#253a86" text-anchor="middle">$</text></svg>
    <span class="service__title">Funding</span>
    <p class="service__text">Lorem ipsum dolor sit amet, consectetur adipiscing elit, sed do eiusmod tempor incididunt.</p>
  </div>

  <footer class="band band--back">
    <address class="address" style="font-style:normal">Address:<br>0000 Alder Rd #000<br>Fairhaven, OR 0000</address>
    <ul class="contact">
      <li><svg width="8" height="8" viewBox="0 0 8 8"><path d="M2 0l1.5 2L2.5 3.2c.5 1 1.3 1.8 2.3 2.3L6 4.5 8 6 7 8C3.5 7.8.2 4.5 0 1z" fill="#fff"/></svg>(800) 555-0100</li>
      <li><svg width="8" height="8" viewBox="0 0 8 8"><rect x="2" y="0" width="4.5" height="8" rx="1" fill="#fff"/></svg>(503) 555-0100</li>
      <li><svg width="8" height="8" viewBox="0 0 8 8"><rect x="0" y="1.5" width="8" height="5" rx=".5" fill="#fff"/></svg>info@halvernconstruction.com</li>
    </ul>
    <div class="brand brand--footer">
      <div class="brand__mark"></div>
      <div class="brand__name"><span>Halvern</span><span>Construction</span></div>
    </div>
    <span class="site--back">www.halvernconstruction.com</span>
  </footer>
</section>

</body>
</html>
```